Brandvale Site Oversight Group Inc. needs a logo design (BSOGI) and a business card design

We need a logo design and business card design for a new company. Simple yet elegant/stylish and professional. to the point. Focal point BRANDVALE...underneith Site Oversight Group Inc smaller font. Plus a logo that can be on the opposite side of the business card and used for T-Shirts.
Back back ground, silver/grey font. I like the look of Quirtle Studio logo
Target Market(s)
Project controls, Planning, Scheduling, Engineering, Project Management
Industry/Entity Type
Business
Contact Information for Business Card
Company name on one side, logo and details on the other
Font styles to use
Requirements
Must have
- Delphine Brandvale
- Project Planner
- BrandvaleSOGI@postmarrow.example
- P.O. Box 9
- Fennrook QX VALDORIA
- X9Q2R7
- +1 (555) 284 3917
Nice to have
- Your input :) quote "Fail to plan, plan to fail"
Should not have
- Too much!

```html
<!DOCTYPE html>
<html lang="en">
<head>
<meta charset="utf-8">
<title>Brandvale Site Oversight Group Inc. — Business Card</title>
<link rel="stylesheet" href="https://fonts.googleapis.com/css2?family=Questrial&display=swap">
<style>
  :root {
    --backdrop: #2b1519;
    --card-white: #f1f1f1;
    --card-dark: #3a3a3a;
    --ink-grey: #5a5a5a;
    --ink-soft: #7a7a7a;
    --ink-dark: #2e2e2e;
    --silver: #b9b9b9;
    --shadow: rgba(0,0,0,0.55);
  }
  * { margin: 0; padding: 0; box-sizing: border-box; }
  html, body { width: 1200px; height: 727px; overflow: hidden; }
  body {
    background: var(--backdrop);
    font-family: "Questrial", "Century Gothic", sans-serif;
    position: relative;
  }
  .card {
    position: absolute;
    top: 203px;
    width: 520px;
    height: 320px;
    border-radius: 22px;
    box-shadow: 0 18px 40px var(--shadow);
  }
  .card--front { left: 50px; background: var(--card-white); color: var(--ink-grey); }
  .card--back { left: 630px; background: var(--card-dark); color: var(--silver); }

  .wordmark { position: absolute; line-height: 1; }
  .wordmark__short { display: block; color: var(--ink-grey); }
  .wordmark__full { display: block; color: var(--ink-grey); letter-spacing: 0.12em; }

  .card--front .wordmark { left: 34px; top: 30px; }
  .card--front .wordmark__short { font-size: 56px; letter-spacing: 0.02em; }
  .card--front .wordmark__full { font-size: 9px; margin-top: 6px; }

  .card--back .wordmark { left: 0; right: 0; top: 98px; text-align: center; }
  .card--back .wordmark__short { font-size: 96px; color: var(--silver); letter-spacing: 0.02em; }
  .card--back .wordmark__full { font-size: 13px; color: var(--silver); margin-top: 12px; letter-spacing: 0.18em; }

  .person { position: absolute; left: 34px; top: 166px; }
  .person__name { font-size: 19px; color: var(--ink-dark); }
  .person__role { font-size: 12px; color: var(--ink-soft); margin-top: 4px; }

  .contact { position: absolute; left: 262px; top: 200px; list-style: none; font-size: 12.5px; color: var(--ink-dark); }
  .contact__item { display: flex; align-items: flex-start; gap: 8px; margin-bottom: 4px; line-height: 1.35; }
  .contact__icon { width: 12px; height: 12px; flex: none; margin-top: 2px; fill: var(--ink-grey); }
</style>
</head>
<body>
  <section class="card card--front" aria-label="Business card front">
    <div class="wordmark">
      <span class="wordmark__short">BSOGI</span>
      <span class="wordmark__full">BRANDVALE SITE OVERSIGHT GROUP INC.</span>
    </div>
    <div class="person">
      <p class="person__name">Delphine Brandvale</p>
      <p class="person__role">Project Planner</p>
    </div>
    <ul class="contact">
      <li class="contact__item">
        <svg class="contact__icon" viewBox="0 0 12 12" aria-hidden="true"><rect x="0" y="2" width="12" height="8" rx="1"/><path d="M0 2 L6 7 L12 2" fill="none" stroke="#f1f1f1" stroke-width="1"/></svg>
        <span>BrandvaleSOGI@postmarrow.example</span>
      </li>
      <li class="contact__item">
        <svg class="contact__icon" viewBox="0 0 12 12" aria-hidden="true"><path d="M1 3 Q6 0 11 3 L10 5 L8 4.5 L8 3.5 Q6 3 4 3.5 L4 4.5 L2 5 Z"/><rect x="2.5" y="5.5" width="7" height="5" rx="1"/></svg>
        <span>+1 (555) 284 3917</span>
      </li>
      <li class="contact__item">
        <svg class="contact__icon" viewBox="0 0 12 12" aria-hidden="true"><path d="M6 0 A4 4 0 0 1 10 4 C10 7 6 12 6 12 C6 12 2 7 2 4 A4 4 0 0 1 6 0 Z M6 2.5 A1.5 1.5 0 1 0 6 5.5 A1.5 1.5 0 1 0 6 2.5 Z"/></svg>
        <span>P.O. Box 9<br>Fennrook QX VALDORIA<br>X9Q2R7</span>
      </li>
    </ul>
  </section>

  <section class="card card--back" aria-label="Business card back">
    <div class="wordmark">
      <span class="wordmark__short">BSOGI</span>
      <span class="wordmark__full">BRANDVALE SITE OVERSIGHT GROUP INC.</span>
    </div>
  </section>
</body>
</html>
```